Homemaking training schools needs a Business Card design

Designer, Hello!

No special requirements, good-looking enough.
--------------------------------------------------------------------------

Name: Marcus Liao
Chairman
Tel: 0574-57418263
Mobile: 13852247106
Email: kelvory@mailpond.com
Web: www.tqb2031.com
Add: No.258, LinfengJie, DaoyueQu, Ningbo, Zhejiang

LOGO
Ningbo TQB Homemaking Training School

Target Market(s)

pregnant women, mothers, infants, the elderly and families, including cleaning, cooking, nursing training.

Industry/Entity Type

Business

Contact Information for Business Card

Name: Marcus Liao
Chairman
Tel: 0574-57418263
Mobile: 13852247106
Email: kelvory@mailpond.com
Web: www.tqb2031.com

LOGO

Font styles to use
Serif
Sans Serif
Decorative

Requirements
Nice to have
• Feels: clean, specifications, safety, comfort, warmth and happiness.

```html
<!DOCTYPE html>
<html lang="en">
<head>
<meta charset="utf-8">
<title>TaoQiBao Business Card</title>
<link href="https://fonts.googleapis.com/css2?family=Montserrat:wght@500;600&family=Open+Sans:wght@400;600&display=swap" rel="stylesheet">
<style>
  :root {
    --stage: #2b2b2b;
    --card: #1b1b1c;
    --red: #d42a2f;
    --red-light: #e8474a;
    --pink: #e5138c;
    --pink-light: #ec3aa0;
    --green: #54b948;
    --green-light: #7cc242;
    --blue: #1b8fcb;
    --blue-light: #22a6dc;
    --text: #ffffff;
    --muted: #cfcfcf;
  }
  * { box-sizing: border-box; margin: 0; padding: 0; }
  html, body { width: 1200px; height: 1200px; overflow: hidden; }
  body { background: var(--stage); position: relative; font-family: "Open Sans", Arial, sans-serif; }

  .card { position: absolute; background: var(--card); overflow: hidden; box-shadow: 0 18px 40px rgba(0,0,0,.55); }

  /* ---------- Brand name (plain text placeholder) ---------- */
  .brand { position: absolute; display: flex; flex-direction: column; align-items: flex-start; }
  .brand__name { font-family: "Montserrat", Arial, sans-serif; font-weight: 500; color: var(--text); letter-spacing: .5px; line-height: 1.1; }
  .brand__tagline { font-family: "Montserrat", Arial, sans-serif; font-weight: 500; color: var(--muted); margin-top: 8px; }

  /* ---------- Front (portrait) ---------- */
  .card--front { left: 70px; top: 250px; width: 400px; height: 700px; }
  .card--front .brand { left: 70px; top: 95px; }
  .card--front .brand__name { font-size: 40px; }
  .card--front .brand__tagline { font-size: 13px; }

  .bands { position: absolute; left: 60px; right: 0; top: 250px; display: flex; flex-direction: column; gap: 22px; }
  .band { display: flex; height: 92px; }
  .band__icon { width: 84px; flex: none; display: flex; align-items: center; justify-content: center; }
  .band__icon svg { width: 30px; height: 30px; fill: none; stroke: var(--text); stroke-width: 2; }
  .band__icon svg .solid { fill: var(--text); stroke: none; }
  .band__body { flex: 1; display: flex; flex-direction: column; justify-content: center; padding-left: 22px; color: var(--text); font-size: 14px; line-height: 1.45; letter-spacing: .4px; }

  .band--name .band__icon { background: var(--red-light); }
  .band--name .band__body { background: var(--red); }
  .band--address .band__icon { background: var(--pink-light); }
  .band--address .band__body { background: var(--pink); }
  .band--phone .band__icon { background: var(--green-light); }
  .band--phone .band__body { background: var(--green); }
  .band--web .band__icon { background: var(--blue-light); }
  .band--web .band__body { background: var(--blue); }

  .person__name { font-family: "Montserrat", Arial, sans-serif; font-weight: 600; font-size: 22px; letter-spacing: 1.5px; text-transform: uppercase; line-height: 1.1; }
  .person__title { font-size: 11px; font-weight: 600; align-self: flex-end; margin-right: 40px; margin-top: -2px; }

  /* ---------- Back (landscape) ---------- */
  .card--back { left: 520px; top: 420px; width: 620px; height: 370px; }
  .strip { position: absolute; display: flex; }
  .strip span { width: 72px; height: 42px; display: block; }
  .strip--top { left: 0; top: 0; }
  .strip--bottom { right: 0; bottom: 0; }
  .swatch--red { background: var(--red); }
  .swatch--pink { background: var(--pink); }
  .swatch--green { background: var(--green); }
  .swatch--blue { background: var(--blue); }

  .card--back .brand { left: 50%; top: 135px; transform: translateX(-50%); align-items: center; }
  .card--back .brand__name { font-size: 46px; }
  .card--back .brand__tagline { font-size: 14px; }

  .back__web { position: absolute; right: 300px; bottom: 14px; color: var(--text); font-size: 12px; letter-spacing: .6px; }
</style>
</head>
<body>

<section class="card card--front" aria-label="Business card front">
  <div class="brand">
    <span class="brand__name">TaoQiBao</span>
    <span class="brand__tagline">Training &amp; Services</span>
  </div>

  <div class="bands">
    <div class="band band--name">
      <div class="band__icon">
        <svg viewBox="0 0 24 24" aria-hidden="true"><circle class="solid" cx="12" cy="8" r="4.5"/><path class="solid" d="M3 21c0-5 4-7.5 9-7.5s9 2.5 9 7.5z"/></svg>
      </div>
      <div class="band__body">
        <span class="person__name">Marcus Liao</span>
        <span class="person__title">Chairman</span>
      </div>
    </div>

    <div class="band band--address">
      <div class="band__icon">
        <svg viewBox="0 0 24 24" aria-hidden="true"><path class="solid" d="M12 3 2 12h3v9h5v-6h4v6h5v-9h3z"/></svg>
      </div>
      <div class="band__body">
        <span>No.258, LinfengJie, DaoyueQu,</span>
        <span>Ningbo, Zhejiang</span>
      </div>
    </div>

    <div class="band band--phone">
      <div class="band__icon">
        <svg viewBox="0 0 24 24" aria-hidden="true"><rect x="6.5" y="2.5" width="11" height="19" rx="2"/><line x1="10" y1="18.5" x2="14" y2="18.5"/></svg>
      </div>
      <div class="band__body">
        <span>0574-57418263</span>
        <span>13852247106</span>
      </div>
    </div>

    <div class="band band--web">
      <div class="band__icon">
        <svg viewBox="0 0 24 24" aria-hidden="true"><circle cx="12" cy="12" r="9"/><ellipse cx="12" cy="12" rx="4" ry="9"/><line x1="3" y1="12" x2="21" y2="12"/><line x1="4.5" y1="7.5" x2="19.5" y2="7.5"/><line x1="4.5" y1="16.5" x2="19.5" y2="16.5"/></svg>
      </div>
      <div class="band__body">
        <span>kelvory@mailpond.com</span>
        <span>www.tqb2031.com</span>
      </div>
    </div>
  </div>
</section>

<section class="card card--back" aria-label="Business card back">
  <div class="strip strip--top">
    <span class="swatch--red"></span><span class="swatch--pink"></span><span class="swatch--green"></span><span class="swatch--blue"></span>
  </div>
  <div class="brand">
    <span class="brand__name">TaoQiBao</span>
    <span class="brand__tagline">Training &amp; Services</span>
  </div>
  <div class="back__web">www.tqb2031.com</div>
  <div class="strip strip--bottom">
    <span class="swatch--blue"></span><span class="swatch--green"></span><span class="swatch--pink"></span><span class="swatch--red"></span>
  </div>
</section>

</body>
</html>
```